PowerPoint Design for a Biotech Consulting Firm

We need a powerpoint design for a new business based in Philadelphia called VorentaRx. This is a consulting firm that will serve medical diagnostics industry, which is part of the life science/healthcare industry focusing on developing and marketing products that help in early detection, monitoring or management of diseases. Our consulting firm will help medical diagnostic companies to overcome key challenges in designing, evaluating and marketing new products.Our company name is VorentaRx. Vorenta is Latin word for "something", Dx represents diagnostics. The idea behind the name is that we help companies to transform the original, early product ideas ("nothing") into "something" which is a product with full clinical utility that will help to improve health and well-being.The powerpoint should use the visual feel of the logo (attached), be modern, simple and clean looking and represent creativity, innovation, scientific thinking and progress.

Target Market(s)

Biotech

Industry/Entity Type

Biotechnology

Font styles to use
Sans Serif

Colors
0355a3
3276b5
85abd2
cfdeed
ffffff
959595
aaaaaa
cbcbcb
070707

Requirements
Must have
• - look and feel, logo colors
• - multiple slide formats

```html
<!DOCTYPE html>
<html lang="en">
<head>
<meta charset="utf-8">
<title>VorentaRx Presentation Design</title>
<link href="https://fonts.googleapis.com/css2?family=Roboto:wght@400;500;700&display=swap" rel="stylesheet">
<style>
:root{
  --navy:#0355a3;
  --mid:#3276b5;
  --soft:#85abd2;
  --pale:#cfdeed;
  --white:#ffffff;
  --grey:#959595;
  --grey-2:#aaaaaa;
  --grey-3:#cbcbcb;
  --ink:#070707;
  --bright:#1f86f7;
  --text:#4a4a4a;
  --heading:#4d4d4d;
  --stage:#e9eef5;
}
*{box-sizing:border-box;margin:0;padding:0}
html,body{width:1011px;height:1200px;overflow:hidden}
body{background:var(--stage);font-family:'Roboto',sans-serif;color:var(--text);position:relative}
.slide{position:absolute;width:318px;height:178px;background:var(--white);overflow:hidden;box-shadow:0 2px 6px rgba(0,0,0,.18)}
.abs{position:absolute}
.brand{font-family:'Roboto',sans-serif;font-weight:500;color:var(--heading);white-space:nowrap;letter-spacing:.2px}
.brand-sm{font-size:5px}
.p{font-size:4.2px;line-height:1.32;color:var(--text);text-align:justify}
.h{font-weight:500;line-height:1.05;color:var(--heading);text-transform:uppercase}
.h .blue{color:var(--bright)}
.blue{color:var(--bright)}
.photo{position:absolute}
.label{position:absolute;font-size:5.5px;color:var(--white);padding:1px 4px;letter-spacing:.2px}

.s-title{left:10px;top:106px;width:650px;height:366px}
.s-title .title{left:30px;top:118px;font-size:33px;font-weight:700}
.s-title .band{left:0;top:163px;width:525px;height:120px;background:rgba(31,134,247,.78)}
.s-title .band-text{left:17px;top:180px;width:392px;font-size:8.6px;line-height:1.48;color:var(--white);text-align:justify}

.logo-tile{position:absolute;left:682px;top:22px;width:318px;height:168px;display:flex;align-items:center;justify-content:center}
.logo-tile .brand{font-size:40px}

.s-text{left:682px;top:210px;background:var(--bright)}
.s-content{left:682px;top:402px}
.s-two{left:10px;top:605px}
.s-full{left:346px;top:605px}
.s-process{left:682px;top:605px}
.s-area{left:10px;top:800px}
.s-3d{left:346px;top:800px}
.s-cluster{left:682px;top:800px}
.s-services{left:10px;top:995px}
.s-donut{left:346px;top:995px}
.s-stacked{left:682px;top:995px}
.axis{font-size:5px;fill:var(--ink)}
.cat{font-size:4.6px;fill:var(--ink)}
.money{font-size:9px;font-weight:700;color:var(--ink);text-align:center}
.cap{font-size:3.6px;text-align:center;line-height:1.3}
</style>
</head>
<body>

<section class="slide s-title">
  <div class="abs brand" style="left:33px;top:42px;font-size:7px">VorentaRx</div>
  <h1 class="abs h title">Title <span class="blue">Here</span></h1>
  <div class="photo" style="left:317px;top:9px;width:144px;height:104px;background:linear-gradient(135deg,#d86a2a,#b0238f 45%,#3d2a9a 75%,#141428)" role="img" aria-label="Laboratory flasks with coloured liquid"></div>
  <div class="photo" style="left:472px;top:9px;width:143px;height:104px;background:radial-gradient(circle at 55% 75%,#2b6fd6,#0a1c44 55%,#000)" role="img" aria-label="Blue glass flask on black"></div>
  <div class="photo" style="left:317px;top:126px;width:144px;height:104px;background:radial-gradient(circle at 30% 30%,#e7772e,#5a1e10 50%,#000)" role="img" aria-label="Orange flask detail"></div>
  <div class="photo" style="left:472px;top:126px;width:143px;height:104px;background:radial-gradient(circle at 40% 45%,#37a6f0,#0d3a6a 50%,#000)" role="img" aria-label="Blue flask detail"></div>
  <div class="photo" style="left:317px;top:244px;width:144px;height:104px;background:#020202" role="img" aria-label="Dark laboratory backdrop"></div>
  <div class="photo" style="left:472px;top:244px;width:143px;height:104px;background:#020202" role="img" aria-label="Dark laboratory backdrop"></div>
  <div class="abs band"></div>
  <p class="abs band-text"><b>Far far away,</b> behind the word mountains, far from the countries Vokalia and Consonantia, there live the blind texts. Separated they live in Bookmarksgrove right at the coast of the Semantics, a large language ocean.<br>Lorem ipsum dolor sit amet, consectetur adipiscing elit. Sed eleifend, diam vitae auctor consequat, dui erat efficitur enim. Far far away, behind the word mountains, far from the countries Vokalia and Consonantia, there live the blind texts. Separated they live in Bookmarksgrove right at the coast of the Semantics, a large language ocean.</p>
</section>

<div class="logo-tile"><span class="brand">VorentaRx</span></div>

<section class="slide s-text">
  <div class="abs" style="left:16px;top:24px;width:80px;color:#fff;font-size:4.2px;line-height:1.35">
    <p><span style="font-size:8px">1.</span> <b>Far far away,</b> behind the word mountains, far from the countries, there live the blind texts in quiet rows.</p>
    <p style="margin-top:10px"><span style="font-size:8px">2.</span> Far far away, behind the word mountains, far from the countries, there live the blind texts in quiet rows.</p>
    <p style="margin-top:10px"><span style="font-size:8px">3.</span> Far far away, behind the word mountains, far from the countries, there live the blind texts in quiet rows.</p>
  </div>
  <div class="photo" style="left:106px;top:0;width:96px;height:178px;background:linear-gradient(160deg,#c0237f,#1a8a8a 35%,#d8692a 60%,#0b2e3a 85%,#05080c)" role="img" aria-label="Flasks with teal and orange liquid"></div>
  <div class="abs brand" style="right:10px;top:30px;font-size:9px;color:#fff">VorentaRx</div>
  <div class="abs h" style="right:14px;top:74px;font-size:17px;color:#fff;text-align:right">Your text<br>here</div>
  <p class="abs" style="right:16px;top:128px;width:84px;font-size:4.2px;line-height:1.35;color:#fff;text-align:center"><b>Far far away,</b> behind the word mountains, far from the countries, there live the blind texts.</p>
</section>

<section class="slide s-content">
  <svg class="abs" width="318" height="178" viewBox="0 0 318 178"><polygon points="0,0 45,0 78,24 78,160 222,160 244,178 0,178" fill="var(--bright)"/></svg>
  <div class="photo" style="left:78px;top:19px;width:170px;height:144px;background:linear-gradient(120deg,#e6edf7,#a9c6ea 45%,#5b9ad8 70%,#1d4f95)" role="img" aria-label="Business chart printout with lab glassware"></div>
  <div class="label" style="left:15px;top:25px;width:90px;background:var(--grey);text-align:center">CONTENT 1</div>
  <p class="abs" style="left:8px;top:38px;width:66px;font-size:4px;line-height:1.36;color:#fff"><b>Far far away,</b> behind the word mountains, far from the countries, there live the blind texts. Separated they live in a town at the coast of a large language ocean. Lorem ipsum dolor sit amet, consectetur adipiscing elit. Sed eleifend, diam vitae auctor consequat, dui erat efficitur enim. Lorem ipsum dolor sit amet, consectetur adipiscing elit, diam vitae auctor consequat.</p>
  <div class="label" style="left:210px;top:44px;width:90px;background:#333">CONTENT 2</div>
  <p class="abs" style="left:252px;top:60px;width:56px;font-size:4px;line-height:1.36;color:var(--text)"><b>Far far away,</b> behind the word mountains, far from the countries, there live the blind texts. Separated they live in a town at the coast of the Semantics, a large language ocean. Lorem ipsum dolor sit amet, consectetur adipiscing elit. Sed eleifend, diam vitae auctor consequat, dui erat efficitur enim.</p>
  <div class="abs brand brand-sm" style="right:10px;top:14px">VorentaRx</div>
</section>

<section class="slide s-two">
  <div class="abs brand" style="left:20px;top:32px;font-size:8px">VorentaRx</div>
  <div class="abs h" style="left:16px;top:74px;font-size:17px">Full text<br><span class="blue">two<br>column</span></div>
  <div class="abs" style="left:16px;top:146px;font-size:7px">Your subtitle here</div>
  <p class="abs p" style="left:106px;top:10px;width:98px">Lorem ipsum dolor sit amet, consectetur adipiscing elit. Proin in dui vitae elit rutrum vestibulum eu at ex. Sed vulputate condimentum tincidunt. Vivamus urna odio, rutrum nec leo et, pellentesque rutrum mauris.<br><br>Vivamus sed urna a purus volutpat condimentum. Fusce lobortis lorem vitae massa euismod, ac feugiat nisi sodales. Proin volutpat arcu et sapien ullamcorper tristique. Donec urna ipsum, sollicitudin ut tempus eu, feugiat congue felis. Aenean blandit suscipit lobortis. Cras eu leo arcu.<br><br>Ut malesuada mauris vitae sapien tempus finibus. In luctus felis sit amet iaculis accumsan. Cras sed nunc nibh. In pharetra, justo quis tempus feugiat, odio nulla scelerisque tellus, ac semper lorem justo at velit. Vivamus sed pharetra ipsum. Fusce posuere lacinia nisi, non maximus risus tristique et.</p>
  <p class="abs p" style="left:212px;top:10px;width:98px">Nunc nec sem urna. Cum sociis natoque penatibus et magnis dis parturient montes, nascetur ridiculus mus. Aenean pharetra dignissim lacus et scelerisque. Ut pulvinar erat in nisi laoreet porta. Nam sit amet dignissim augue. Aenean consequat id metus sit amet dapibus. In consequat eget tellus ac iaculis. Praesent vitae sollicitudin est.<br><br>Vivamus sed urna a purus volutpat condimentum. Fusce lobortis lorem vitae massa euismod, ac feugiat nisi sodales. Proin volutpat arcu et sapien ullamcorper tristique. Donec urna ipsum, feugiat congue felis. Aenean blandit suscipit lobortis. Cras eu leo arcu. Vivamus sed urna a purus volutpat condimentum. Proin volutpat arcu et sapien ullamcorper. Donec urna ipsum, sollicitudin ut tempus eu, feugiat congue felis.</p>
</section>

<section class="slide s-full">
  <div class="abs brand" style="left:20px;top:32px;font-size:8px">VorentaRx</div>
  <div class="abs h" style="left:16px;top:74px;font-size:17px">Full text<br><span class="blue">width</span></div>
  <div class="abs" style="left:16px;top:120px;font-size:7px">Your subtitle here</div>
  <p class="abs p" style="left:112px;top:10px;width:196px">Lorem ipsum dolor sit amet, consectetur adipiscing elit. Proin in dui vitae elit rutrum vestibulum eu at ex. Sed vulputate condimentum tincidunt. Vivamus urna odio, rutrum nec leo et, pellentesque rutrum mauris.<br><br>Vivamus sed urna a purus volutpat condimentum. Fusce lobortis lorem vitae massa euismod, ac feugiat nisi sodales. Proin volutpat arcu et sapien ullamcorper tristique. Donec urna ipsum, sollicitudin ut tempus eu, feugiat congue felis. Aenean blandit suscipit lobortis. Cras eu leo arcu.<br><br>Ut malesuada mauris vitae sapien tempus finibus. In luctus felis sit amet iaculis accumsan. Cras sed nunc nibh. In pharetra, justo quis tempus feugiat, odio nulla scelerisque tellus, ac semper lorem justo at velit. Vivamus sed pharetra ipsum. Fusce posuere lacinia nisi, non maximus risus tristique et. Vestibulum cursus dolor non lectus fermentum volutpat. Vivamus luctus turpis et arcu condimentum, ac viverra erat gravida. Nunc nec sem urna. Cum sociis natoque penatibus et magnis dis parturient montes, nascetur ridiculus mus. Aenean pharetra dignissim lacus et scelerisque. Ut pulvinar erat in nisi laoreet porta.<br><br>Vivamus sed urna a purus volutpat condimentum. Fusce lobortis lorem vitae massa euismod, ac feugiat nisi sodales. Donec urna ipsum, sollicitudin ut tempus eu, feugiat congue felis. Aenean blandit suscipit lobortis. Cras eu leo arcu.</p>
</section>

<section class="slide s-process">
  <div class="abs brand brand-sm" style="left:18px;top:24px">VorentaRx</div>
  <div class="abs h" style="left:0;top:12px;width:100%;text-align:center;font-size:15px;padding-left:10px">Our<br><span class="blue">business process</span></div>
  <svg class="abs" width="318" height="178" viewBox="0 0 318 178">
    <path d="M60 124 L88 132 L120 108 L164 128 L222 88" stroke="var(--soft)" stroke-width="10" fill="none" stroke-linejoin="round"/>
    <circle cx="60" cy="124" r="12" fill="var(--mid)"/>
    <circle cx="92" cy="132" r="14" fill="var(--grey)"/>
    <circle cx="126" cy="108" r="20" fill="var(--navy)"/>
    <circle cx="174" cy="128" r="24" fill="var(--ink)"/>
    <circle cx="224" cy="86" r="32" fill="var(--bright)"/>
    <g fill="none" stroke="#fff" stroke-width=".8" opacity=".8">
      <rect x="221" y="81" width="7" height="10"/><rect x="171" y="123" width="7" height="10"/><rect x="123" y="103" width="6" height="9"/><rect x="89" y="128" width="5" height="7"/>
    </g>
  </svg>
  <div class="abs" style="left:108px;top:58px;width:50px;text-align:center;font-size:4px;line-height:1.3"><b style="font-size:5px">Poin Name Here</b><br>Lorem ipsum dolor sit amet, consectetur</div>
  <div class="abs" style="left:32px;top:75px;width:50px;text-align:center;font-size:4px;line-height:1.3"><b style="font-size:5px">Poin Name Here</b><br>Lorem ipsum dolor sit amet, consectetur</div>
  <div class="abs" style="left:258px;top:108px;width:52px;text-align:center;font-size:4px;line-height:1.3"><b style="font-size:5px">Poin Name Here</b><br>Lorem ipsum dolor sit amet, consectetur</div>
  <div class="abs" style="left:218px;top:140px;width:52px;text-align:center;font-size:4px;line-height:1.3"><b style="font-size:5px">Poin Name Here</b><br>Lorem ipsum dolor sit amet, consectetur</div>
  <div class="abs" style="left:34px;top:148px;width:52px;text-align:center;font-size:4px;line-height:1.3"><b style="font-size:5px">Poin Name Here</b><br>Lorem ipsum dolor sit amet, consectetur</div>
</section>

<section class="slide s-area">
  <div class="abs brand brand-sm" style="left:18px;top:22px">VorentaRx</div>
  <svg class="abs" width="170" height="178" viewBox="0 0 170 178">
    <g stroke="#dcdcdc" stroke-width=".4">
      <line x1="34" y1="50" x2="166" y2="50"/><line x1="34" y1="65" x2="166" y2="65"/><line x1="34" y1="80" x2="166" y2="80"/><line x1="34" y1="95" x2="166" y2="95"/><line x1="34" y1="110" x2="166" y2="110"/><line x1="34" y1="125" x2="166" y2="125"/>
    </g>
    <polygon points="34,80 60,93 86,72 110,94 140,82 166,64 166,140 34,140" fill="var(--mid)"/>
    <polygon points="34,110 80,108 110,96 166,66 166,140 34,140" fill="var(--soft)"/>
    <g class="axis" text-anchor="end"><text x="28" y="52">6</text><text x="28" y="67">5</text><text x="28" y="82">4</text><text x="28" y="97">3</text><text x="28" y="112">2</text><text x="28" y="127">1</text><text x="28" y="142">0</text></g>
  </svg>
  <div class="abs h" style="left:186px;top:46px;font-size:15px">Area <span class="blue">chart</span></div>
  <div class="abs" style="left:186px;top:66px;font-size:6px;font-weight:500;color:var(--ink)">Area Chart</div>
  <p class="abs p" style="left:186px;top:74px;width:118px;text-align:left">Lorem ipsum dolor sit amet, consectetur adipiscing elit. Proin sed libero in magna ultrices gravida sit amet at diam. Suspendisse placerat gravida magna vel fermentum.</p>
  <svg class="abs" style="left:196px;top:106px" width="10" height="10"><circle cx="5" cy="5" r="3.2" fill="var(--bright)"/></svg>
  <svg class="abs" style="left:256px;top:106px" width="16" height="10"><g stroke="var(--mid)" stroke-width="1.2"><line x1="1" y1="2" x2="15" y2="2"/><line x1="1" y1="5" x2="15" y2="5"/><line x1="1" y1="8" x2="15" y2="8"/></g></svg>
  <div class="abs" style="left:180px;top:118px;width:42px;text-align:center;font-size:3.8px;line-height:1.35">Subtitle Here<br><b style="font-size:5.5px;color:var(--ink)">Main Title</b><br><br>Lorem ipsum dolor sit amet, consectetur adipiscing elit.</div>
  <div class="abs" style="left:243px;top:118px;width:42px;text-align:center;font-size:3.8px;line-height:1.35">Subtitle Here<br><b style="font-size:5.5px;color:var(--ink)">Main Title</b><br><br>Lorem ipsum dolor sit amet, consectetur adipiscing elit.</div>
</section>

<section class="slide s-3d">
  <div class="abs brand brand-sm" style="right:10px;top:20px">VorentaRx</div>
  <div class="abs h" style="left:20px;top:32px;font-size:15px">Clustered<br><span class="blue">column</span></div>
  <div class="abs" style="left:148px;top:36px;font-size:6px;font-weight:500;color:var(--ink)">3D Clustered Column</div>
  <p class="abs p" style="left:148px;top:44px;width:140px;text-align:left">Lorem ipsum dolor sit amet, consectetur adipiscing elit. Proin sed libero in magna ultrices gravida sit amet at diam. Suspendisse placerat gravida magna vel fermentum. Aenean nunc purus, consequat vitae interdum eget,</p>
  <svg class="abs" width="318" height="178" viewBox="0 0 318 178">
    <g class="axis" text-anchor="end"><text x="44" y="88">5</text><text x="44" y="102">4</text><text x="44" y="116">3</text><text x="44" y="130">2</text><text x="44" y="144">1</text><text x="44" y="158">0</text></g>
    <line x1="50" y1="156" x2="292" y2="156" stroke="var(--grey-3)" stroke-width=".6"/>
    <g>
      <rect x="64" y="96" width="14" height="60" fill="var(--grey)"/><rect x="78" y="122" width="14" height="34" fill="var(--navy)"/><rect x="92" y="128" width="14" height="28" fill="var(--soft)"/>
      <rect x="124" y="121" width="14" height="35" fill="var(--grey)"/><rect x="138" y="94" width="14" height="62" fill="var(--navy)"/><rect x="152" y="128" width="14" height="28" fill="var(--soft)"/>
      <rect x="184" y="107" width="14" height="49" fill="var(--grey)"/><rect x="198" y="131" width="14" height="25" fill="var(--navy)"/><rect x="212" y="114" width="14" height="42" fill="var(--soft)"/>
      <rect x="244" y="93" width="14" height="63" fill="var(--grey)"/><rect x="258" y="117" width="14" height="39" fill="var(--navy)"/><rect x="272" y="86" width="14" height="70" fill="var(--soft)"/>
    </g>
    <g class="cat" text-anchor="middle" font-size="4.4"><text x="71" y="94">4.3</text><text x="85" y="120">2.4</text><text x="99" y="126">2</text><text x="131" y="119">2.5</text><text x="145" y="92">4.4</text><text x="159" y="126">2</text><text x="191" y="105">3.5</text><text x="205" y="129">1.8</text><text x="219" y="112">3</text><text x="251" y="91">4.5</text><text x="265" y="115">2.8</text><text x="279" y="84">5</text></g>
    <g class="cat" text-anchor="middle"><text x="85" y="166">Category 1</text><text x="145" y="166">Category 2</text><text x="205" y="166">Category 3</text><text x="265" y="166">Category 4</text></g>
  </svg>
</section>

<section class="slide s-cluster">
  <div class="abs brand brand-sm" style="left:18px;top:22px">VorentaRx</div>
  <div class="abs h" style="left:14px;top:42px;font-size:15px">Clustered<br><span class="blue">column</span></div>
  <div class="abs" style="left:14px;top:92px;font-size:6px;color:var(--ink)">Clustered Column</div>
  <p class="abs p" style="left:14px;top:100px;width:110px;text-align:left">Lorem ipsum dolor sit amet, consectetur adipiscing elit. Proin sed libero in magna ultrices gravida sit amet at diam. Suspendisse placerat gravida magna vel fermentum. Aenean nunc purus, consequat vitae interdum eget,</p>
  <svg class="abs" width="318" height="178" viewBox="0 0 318 178">
    <g stroke="#e2e2e2" stroke-width=".4"><line x1="146" y1="36" x2="294" y2="36"/><line x1="146" y1="51" x2="294" y2="51"/><line x1="146" y1="66" x2="294" y2="66"/><line x1="146" y1="81" x2="294" y2="81"/><line x1="146" y1="96" x2="294" y2="96"/><line x1="146" y1="111" x2="294" y2="111"/><line x1="146" y1="126" x2="294" y2="126"/></g>
    <g class="axis" text-anchor="end"><text x="140" y="38">6</text><text x="140" y="53">5</text><text x="140" y="68">4</text><text x="140" y="83">3</text><text x="140" y="98">2</text><text x="140" y="113">1</text><text x="140" y="128">0</text></g>
    <rect x="152" y="61" width="5" height="65" fill="var(--navy)"/><rect x="158" y="90" width="5" height="36" fill="var(--mid)"/><rect x="164" y="96" width="5" height="30" fill="#a9bde0"/>
    <rect x="190" y="88" width="5" height="38" fill="var(--navy)"/><rect x="196" y="60" width="5" height="66" fill="var(--mid)"/><rect x="202" y="96" width="5" height="30" fill="#a9bde0"/>
    <rect x="228" y="73" width="5" height="53" fill="var(--navy)"/><rect x="234" y="99" width="5" height="27" fill="var(--mid)"/><rect x="240" y="81" width="5" height="45" fill="#a9bde0"/>
    <rect x="266" y="58" width="5" height="68" fill="var(--navy)"/><rect x="272" y="84" width="5" height="42" fill="var(--mid)"/><rect x="278" y="51" width="5" height="75" fill="#a9bde0"/>
  </svg>
</section>

<section class="slide s-services">
  <div class="photo" style="left:12px;top:22px;width:54px;height:58px;background:linear-gradient(135deg,#6b8fa8,#c9d7e2 55%,#8aa8bd)" role="img" aria-label="Scientist working in a laboratory"></div>
  <div class="label" style="left:52px;top:68px;background:#333">SERVICE 1</div>
  <p class="abs" style="left:66px;top:82px;width:46px;font-size:3.4px;line-height:1.3"><b>Far far away,</b> behind the word mountains, far from the countries, there live the blind texts.</p>
  <div class="photo" style="left:100px;top:4px;width:54px;height:44px;background:linear-gradient(135deg,#b8c3cc,#eef2f5 55%,#7fb0cf)" role="img" aria-label="Microscope and sample tubes"></div>
  <div class="label" style="left:142px;top:46px;background:#333">SERVICE 2</div>
  <p class="abs" style="left:160px;top:18px;width:46px;font-size:3.4px;line-height:1.3"><b>Far far away,</b> behind the word mountains, far from the countries, there live the blind texts.</p>
  <div class="photo" style="left:126px;top:72px;width:54px;height:60px;background:linear-gradient(135deg,#a7c2d6,#e6edf2 50%,#3c88c7)" role="img" aria-label="Pipette over a sample dish"></div>
  <div class="label" style="left:156px;top:118px;background:#333">SERVICE 4</div>
  <p class="abs" style="left:160px;top:132px;width:46px;font-size:3.4px;line-height:1.3"><b>Far far away,</b> behind the word mountains, far from the countries, there live the blind texts.</p>
  <div class="photo" style="left:30px;top:110px;width:54px;height:60px;background:linear-gradient(135deg,#d7e4f2,#5f9ad8 60%,#3fa9a0)" role="img" aria-label="Chart printout with lab glassware"></div>
  <div class="label" style="left:76px;top:122px;background:#333">SERVICE 3</div>
  <p class="abs" style="left:88px;top:134px;width:46px;font-size:3.4px;line-height:1.3"><b>Far far away,</b> behind the word mountains, far from the countries, there live the blind texts.</p>
  <div class="abs brand brand-sm" style="right:10px;top:22px">VorentaRx</div>
  <div class="abs h" style="right:10px;top:52px;font-size:15px;text-align:right;color:var(--grey)">Our great<br><span class="blue">services</span></div>
  <p class="abs" style="right:10px;top:100px;width:100px;font-size:4px;line-height:1.36;text-align:right;color:var(--grey)"><b>Far far away,</b> behind the word mountains, far from the countries, there live the blind texts. Separated they live in a town at the coast of the Semantics, a large language ocean.</p>
</section>

<section class="slide s-donut">
  <div class="abs brand brand-sm" style="left:18px;top:24px">VorentaRx</div>
  <div class="abs h" style="left:0;top:22px;width:100%;text-align:center;font-size:15px;padding-left:14px">Doughnut <span class="blue">chart</span></div>
  <div class="abs" style="left:142px;top:84px;font-size:4.4px;color:var(--ink)">CHART</div>
  <svg class="abs" width="318" height="178" viewBox="0 0 318 178">
    <g fill="none" stroke-width="8" transform="rotate(-90)">
      <g transform="translate(-105,48)"><circle r="13" stroke="var(--grey)" pathLength="100" stroke-dasharray="30 70"/><circle r="13" stroke="var(--grey-3)" pathLength="100" stroke-dasharray="25 75" stroke-dashoffset="-30"/><circle r="13" stroke="var(--soft)" pathLength="100" stroke-dasharray="25 75" stroke-dashoffset="-55"/><circle r="13" stroke="var(--mid)" pathLength="100" stroke-dasharray="20 80" stroke-dashoffset="-80"/></g>
      <g transform="translate(-105,120)"><circle r="13" stroke="var(--grey-2)" pathLength="100" stroke-dasharray="10 90"/><circle r="13" stroke="var(--navy)" pathLength="100" stroke-dasharray="22 78" stroke-dashoffset="-10"/><circle r="13" stroke="var(--mid)" pathLength="100" stroke-dasharray="38 62" stroke-dashoffset="-32"/><circle r="13" stroke="var(--pale)" pathLength="100" stroke-dasharray="30 70" stroke-dashoffset="-70"/></g>
      <g transform="translate(-105,192)"><circle r="13" stroke="var(--navy)" pathLength="100" stroke-dasharray="30 70"/><circle r="13" stroke="var(--mid)" pathLength="100" stroke-dasharray="20 80" stroke-dashoffset="-30"/><circle r="13" stroke="var(--soft)" pathLength="100" stroke-dasharray="25 75" stroke-dashoffset="-50"/><circle r="13" stroke="var(--pale)" pathLength="100" stroke-dasharray="25 75" stroke-dashoffset="-75"/></g>
      <g transform="translate(-105,264)"><circle r="13" stroke="var(--grey)" pathLength="100" stroke-dasharray="20 80"/><circle r="13" stroke="var(--navy)" pathLength="100" stroke-dasharray="35 65" stroke-dashoffset="-20"/><circle r="13" stroke="var(--soft)" pathLength="100" stroke-dasharray="15 85" stroke-dashoffset="-55"/><circle r="13" stroke="var(--pale)" pathLength="100" stroke-dasharray="30 70" stroke-dashoffset="-70"/></g>
    </g>
  </svg>
  <div class="abs" style="left:18px;top:126px;width:60px"><div class="money">$52,000</div><p class="cap"><b>Add your title here</b><br>Lorem ipsum dolor sit amet, consectetur adipiscing elit.</p></div>
  <div class="abs" style="left:90px;top:126px;width:60px"><div class="money">$73,000</div><p class="cap"><b>Add your title here</b><br>Lorem ipsum dolor sit amet, consectetur adipiscing elit.</p></div>
  <div class="abs" style="left:162px;top:126px;width:60px"><div class="money">$85,000</div><p class="cap"><b>Add your title here</b><br>Lorem ipsum dolor sit amet, consectetur adipiscing elit.</p></div>
  <div class="abs" style="left:234px;top:126px;width:60px"><div class="money">$22,000</div><p class="cap"><b>Add your title here</b><br>Lorem ipsum dolor sit amet, consectetur adipiscing elit.</p></div>
</section>

<section class="slide s-stacked">
  <div class="abs brand brand-sm" style="left:18px;top:24px">VorentaRx</div>
  <svg class="abs" width="318" height="178" viewBox="0 0 318 178">
    <g fill="none" stroke="#9aa6b2" stroke-width=".5"><polygon points="28,46 142,50 142,140 28,140"/><line x1="32" y1="42" x2="146" y2="46"/><line x1="142" y1="50" x2="146" y2="46"/><line x1="146" y1="46" x2="146" y2="136"/></g>
    <rect x="38" y="62" width="6" height="78" fill="#3a3a3a"/><rect x="44" y="88" width="4" height="52" fill="var(--grey)"/><rect x="48" y="100" width="5" height="40" fill="var(--soft)"/>
    <rect x="64" y="60" width="6" height="80" fill="#3a3a3a"/><rect x="70" y="96" width="4" height="44" fill="var(--grey)"/><rect x="74" y="104" width="5" height="36" fill="var(--soft)"/>
    <rect x="90" y="70" width="6" height="70" fill="#3a3a3a"/><rect x="96" y="104" width="4" height="36" fill="var(--grey)"/><rect x="100" y="96" width="5" height="44" fill="var(--soft)"/>
    <rect x="116" y="60" width="6" height="80" fill="#111"/><rect x="122" y="86" width="4" height="54" fill="var(--grey)"/><rect x="126" y="52" width="6" height="88" fill="var(--soft)"/>
  </svg>
  <div class="abs h" style="left:168px;top:48px;font-size:15px">Clustered<br><span class="blue">column</span></div>
  <div class="abs" style="left:168px;top:94px;font-size:5.4px;font-weight:500;color:var(--ink)">100% Stacked Column</div>
  <p class="abs p" style="left:168px;top:102px;width:118px;text-align:left">Lorem ipsum dolor sit amet, consectetur adipiscing elit. Proin sed libero in magna ultrices gravida sit amet at diam. Suspendisse placerat gravida magna vel fermentum. Aenean nunc purus, consequat vitae interdum eget,</p>
</section>

</body>
</html>
```